A Book Cover For a Book Called "Tamsire"

Attached are two files for the ISBN bar graph for the print version of the cover! Same image, just two different formats.
Updates

Project Deadline Extended Reason: We'd like to see a few more designs, and work with a few of the designs already submitted. Added Tuesday, October 24, 2017

Target Market(s)

young adult female, parents

Colors

Designer to choose colors to be used in the design.

```html
<!DOCTYPE html>
<html lang="en">
<head>
<meta charset="utf-8">
<title>Tamsire – A memoir</title>
<link href="https://fonts.googleapis.com/css2?family=Montserrat:wght@300&family=Great+Vibes&display=swap" rel="stylesheet">
<style>
  :root {
    --night: #0a0819;
    --ivory: #ffffff;
    --satin-light: #f3e6c8;
    --satin-mid: #c9b184;
    --satin-deep: #6b5a3e;
  }
  html, body {
    margin: 0;
    padding: 0;
    overflow: hidden;
    background: var(--night);
  }
  .cover {
    position: relative;
    width: 830px;
    height: 1200px;
    background: var(--night);
    overflow: hidden;
  }
  .cover__artwork {
    position: absolute;
    left: 0;
    top: 90px;
    width: 830px;
    height: 930px;
  }
  .cover__authors {
    position: absolute;
    left: 69px;
    top: 80px;
    margin: 0;
    font-family: "Montserrat", sans-serif;
    font-weight: 300;
    font-size: 34px;
    line-height: 48px;
    color: var(--ivory);
    letter-spacing: 0.2px;
  }
  .cover__title {
    position: absolute;
    left: 0;
    width: 830px;
    top: 870px;
    margin: 0;
    text-align: center;
    font-family: "Great Vibes", cursive;
    font-weight: 400;
    font-size: 190px;
    line-height: 220px;
    color: var(--ivory);
    padding-left: 40px;
    box-sizing: border-box;
  }
  .cover__subtitle {
    position: absolute;
    left: 322px;
    top: 1058px;
    margin: 0;
    font-family: "Montserrat", sans-serif;
    font-weight: 300;
    font-size: 40px;
    line-height: 50px;
    color: var(--ivory);
    letter-spacing: 1px;
  }
</style>
</head>
<body>
  <main class="cover">
    <svg class="cover__artwork" viewBox="0 0 830 930" role="img" aria-label="Photograph of a pair of satin pointe shoes with loose ribbons, lit warmly against a dark background">
      <defs>
        <radialGradient id="satinGlow" cx="0.5" cy="0.5" r="0.5">
          <stop offset="0" stop-color="var(--satin-light)"/>
          <stop offset="0.55" stop-color="var(--satin-mid)"/>
          <stop offset="0.85" stop-color="var(--satin-deep)" stop-opacity="0.5"/>
          <stop offset="1" stop-color="var(--night)" stop-opacity="0"/>
        </radialGradient>
      </defs>
      <ellipse cx="230" cy="560" rx="230" ry="300" fill="url(#satinGlow)"/>
      <ellipse cx="560" cy="480" rx="250" ry="420" fill="url(#satinGlow)"/>
    </svg>

    <p class="cover__authors">Willa Hartley<br>with Nora Bellamy</p>
    <h1 class="cover__title">Tamsire</h1>
    <p class="cover__subtitle">A memoir</p>
  </main>
</body>
</html>
```